Business Card Design for a Software Startup

We'd like to have a business card design. We already have a logo. Basically what we need is a clean design with name, address, cellphone and phone numbers, e-mail and web site address (front) and a space on the back with our logo with the company name on the right side and some texts on the bottom.
We are a development and consulting company in Brazil with highly qualified team of professionals in Java, iOS and Android development and consulting.

Target Market(s)

CIO, IT managers of mid to big size companies

Industry/Entity Type

Business

```html
<!DOCTYPE html>
<html lang="en">
<head>
<meta charset="utf-8">
<title>VANTRO Business Card</title>
<link rel="stylesheet" href="https://fonts.googleapis.com/css2?family=Exo+2:wght@600;700&family=Open+Sans:wght@400&display=swap">
<style>
  :root {
    --page: #e9ebee;
    --card-white: #f5f5f5;
    --navy: #1b3f73;
    --navy-deep: #14325f;
    --cyan: #1fa8e6;
    --blue-mid: #1d6fb8;
    --blue-light: #1aa0e0;
    --blue-dark: #27346e;
    --text-body: #24447a;
    --white: #ffffff;
  }
  * { margin: 0; padding: 0; box-sizing: border-box; }
  html, body { width: 1200px; height: 900px; overflow: hidden; }
  body {
    background: var(--page);
    font-family: "Open Sans", sans-serif;
    position: relative;
  }
  .card {
    position: absolute;
    left: 267px;
    width: 665px;
    height: 380px;
    overflow: hidden;
    box-shadow: 0 6px 18px rgba(0,0,0,0.18);
  }
  .card-front { top: 50px; background: var(--card-white); }
  .card-back {
    top: 470px;
    background: radial-gradient(ellipse at 45% 35%, var(--blue-light) 0%, var(--blue-mid) 40%, var(--blue-dark) 100%);
  }

  /* Front */
  .brand-front {
    position: absolute;
    left: 70px;
    top: 150px;
    display: flex;
    align-items: center;
    gap: 12px;
  }
  .brand-square {
    width: 30px; height: 30px;
    background: var(--navy);
    border-radius: 4px;
  }
  .brand-name {
    font-family: "Exo 2", sans-serif;
    font-weight: 700;
    font-size: 38px;
    letter-spacing: 1px;
    color: var(--navy);
  }
  .person {
    position: absolute;
    right: 72px;
    top: 70px;
    text-align: right;
  }
  .person-name {
    font-family: "Exo 2", sans-serif;
    font-weight: 700;
    font-size: 22px;
    color: var(--navy);
  }
  .person-role {
    font-size: 15px;
    color: var(--cyan);
    margin-top: 2px;
  }
  .contact {
    position: absolute;
    right: 50px;
    top: 160px;
    text-align: right;
    color: var(--text-body);
    font-size: 14px;
    line-height: 1.35;
  }
  .address { margin-bottom: 8px; margin-right: 22px; }
  .contact-line {
    display: flex;
    justify-content: flex-end;
    align-items: center;
    gap: 8px;
    height: 24px;
  }
  .contact-line svg { width: 14px; height: 14px; flex: none; }
  .front-bands {
    position: absolute;
    left: 0; bottom: 0;
    width: 665px; height: 90px;
  }

  /* Back */
  .back-streaks { position: absolute; inset: 0; width: 665px; height: 380px; }
  .brand-back {
    position: absolute;
    left: 0; right: 0;
    top: 150px;
    display: flex;
    justify-content: center;
    align-items: center;
    gap: 14px;
  }
  .brand-back .brand-square { width: 40px; height: 40px; background: var(--white); border-radius: 5px; }
  .brand-back .brand-name { color: var(--white); font-size: 58px; }
  .back-url {
    position: absolute;
    left: 0; right: 0;
    bottom: 40px;
    text-align: center;
    color: var(--white);
    font-size: 14px;
    letter-spacing: 0.5px;
  }
</style>
</head>
<body>

<section class="card card-front">
  <div class="brand-front">
    <span class="brand-square"></span>
    <span class="brand-name">VANTRO</span>
  </div>

  <div class="person">
    <div class="person-name">Leo Carvalho</div>
    <div class="person-role">CEO</div>
  </div>

  <div class="contact">
    <div class="address">88 north cedar street, #210<br>boulder, colorado 80302 - 1144</div>
    <div class="contact-line">
      <span>555 - 210 - 4471</span>
      <svg viewBox="0 0 14 14"><path d="M3 1 C1 2 1 6 4 9 C7 12 11 13 12 11 L10 8.5 L8.5 9.5 C7 9 5 7 4.5 5.5 L5.5 4 Z" fill="var(--cyan)"/></svg>
    </div>
    <div class="contact-line">
      <span>555 - 210 - 4472</span>
      <svg viewBox="0 0 14 14"><rect x="3.5" y="1" width="7" height="12" rx="1.5" fill="var(--cyan)"/><rect x="5" y="3" width="4" height="4" fill="var(--white)"/></svg>
    </div>
    <div class="contact-line">
      <span>lcarvalho@vantro.com</span>
      <svg viewBox="0 0 14 14"><rect x="1" y="3" width="12" height="8" fill="none" stroke="var(--cyan)" stroke-width="1.4"/><path d="M1 3 L7 8 L13 3" fill="none" stroke="var(--cyan)" stroke-width="1.4"/></svg>
    </div>
    <div class="contact-line">
      <span>www.vantro.com</span>
      <svg viewBox="0 0 14 14"><circle cx="7" cy="7" r="5.5" fill="none" stroke="var(--cyan)" stroke-width="1.3"/><ellipse cx="7" cy="7" rx="2.3" ry="5.5" fill="none" stroke="var(--cyan)" stroke-width="1"/><line x1="1.5" y1="7" x2="12.5" y2="7" stroke="var(--cyan)" stroke-width="1"/></svg>
    </div>
  </div>

  <svg class="front-bands" viewBox="0 0 665 90" preserveAspectRatio="none">
    <polygon points="380,90 410,42 665,0 665,90" fill="var(--navy-deep)"/>
    <polygon points="0,78 380,72 372,90 0,90" fill="var(--cyan)"/>
  </svg>
</section>

<section class="card card-back">
  <svg class="back-streaks" viewBox="0 0 665 380" preserveAspectRatio="none">
    <polygon points="0,330 665,10 665,60 0,380" fill="var(--white)" opacity="0.06"/>
    <polygon points="100,380 665,150 665,230 250,380" fill="var(--white)" opacity="0.05"/>
    <polygon points="0,200 460,0 540,0 0,250" fill="var(--white)" opacity="0.04"/>
  </svg>
  <div class="brand-back">
    <span class="brand-square"></span>
    <span class="brand-name">VANTRO</span>
  </div>
  <div class="back-url">www.vantro.com</div>
</section>

</body>
</html>
```